VELANTRA
Mobile Ultrasound
Simple
Danielle Morvek RDMS RDCS RVT
President
P.O. Box 48617 Las Vegas, NV 89120-4861
info@velantramobilescan.example
www.velantramobilescan.example

```html
<!DOCTYPE html>
<html lang="en">
<head>
<meta charset="utf-8">
<title>Velantra Stationery Set</title>
<link href="https://fonts.googleapis.com/css2?family=Montserrat:wght@400;600;700&display=swap" rel="stylesheet">
<style>
:root{
  --board-edge:#8e8e8e;
  --board:#a9a9a9;
  --paper:#ffffff;
  --paper-line:#d9d9d9;
  --brand-blue:#1b7fc3;
  --brand-deep:#12568e;
  --ink:#4a4a4a;
  --ink-soft:#7a7a7a;
  --mark-grey:#6e6e6e;
}
*{margin:0;padding:0;box-sizing:border-box}
html,body{width:1200px;height:684px;overflow:hidden}
body{background:var(--board-edge);font-family:'Montserrat',sans-serif;color:var(--ink);position:relative}
.board{position:absolute;left:12px;top:12px;width:1176px;height:660px;background:var(--board)}
.sheet{position:absolute;background:var(--paper);box-shadow:0 1px 3px rgba(0,0,0,.25)}
.band{position:absolute;left:0;right:0;top:0;background:linear-gradient(90deg,var(--brand-deep),var(--brand-blue) 40%,var(--brand-deep))}
.brand{position:absolute;display:flex;align-items:center;gap:6px;z-index:1}
.brand-dot{border-radius:50%;background:var(--mark-grey);flex:none}
.brand-dot.lifted{transform:translateY(-9px)}
.brand-words{display:flex;flex-direction:column;line-height:1}
.brand-name{font-weight:700;color:var(--brand-blue);letter-spacing:.04em}
.brand-tag{font-weight:600;color:var(--ink-soft);letter-spacing:.18em;margin-top:2px}
.fine{position:absolute;font-size:5.5px;line-height:1.6;color:var(--ink);white-space:nowrap}
.fine .icon{display:inline-block;width:5px;height:5px;border-radius:50%;background:var(--brand-blue);margin-right:3px;vertical-align:-1px}
.web{position:absolute;font-size:5.5px;font-weight:600;color:var(--ink);white-space:nowrap}

/* letterhead */
.letterhead{left:185px;top:41px;width:415px;height:597px}
.letterhead .band{height:22px}
.letterhead .brand{left:18px;top:30px}

/* business card */
.card{left:5px;top:271px;width:201px;height:125px;z-index:2}
.card .band{height:10px}
.card .brand{left:12px;top:20px}

/* envelope back */
.env-back{left:636px;top:84px;width:535px;height:223px}
.flap{position:absolute;inset:0;width:100%;height:100%}
.env-back .brand{left:50%;top:58px;transform:translateX(-50%)}

/* envelope front */
.env-front{left:636px;top:365px;width:535px;height:276px}
.env-front .band{height:22px}
.env-front .brand{left:18px;top:30px}
</style>
</head>
<body>
<div class="board">

  <div class="sheet letterhead">
    <div class="band"></div>
    <div class="brand">
      <span class="brand-dot lifted" style="width:26px;height:26px"></span>
      <div class="brand-words"><span class="brand-name" style="font-size:15px">VELANTRA</span><span class="brand-tag" style="font-size:4.5px">MOBILE ULTRASOUND</span></div>
    </div>
    <div class="fine" style="left:24px;top:565px">
      <div><span class="icon"></span>P.O. Box 48617 Las Vegas, NV 89120-4861</div>
      <div><span class="icon"></span>702.555.0148 &nbsp;|&nbsp; info@velantramobilescan.example</div>
    </div>
    <div class="web" style="right:10px;top:576px">www.velantramobilescan.example</div>
  </div>

  <div class="sheet card">
    <div class="band"></div>
    <div class="brand">
      <span class="brand-dot" style="width:22px;height:22px"></span>
      <div class="brand-words"><span class="brand-name" style="font-size:14px">VELANTRA</span><span class="brand-tag" style="font-size:4px">MOBILE ULTRASOUND</span></div>
    </div>
    <div class="fine" style="left:12px;top:60px;font-size:5px">
      <div style="font-weight:600">Danielle Morvek RDMS RDCS RVT &nbsp;|&nbsp; President</div>
      <div style="margin-top:6px"><span class="icon"></span>mlorvek@velantramobilescan.example</div>
      <div><span class="icon"></span>P.O. Box 48617 Las Vegas, NV 89120-4861</div>
      <div><span class="icon"></span>T 702.555.0148 &nbsp;F 702.555.0149</div>
    </div>
  </div>

  <div class="sheet env-back">
    <svg class="flap" viewBox="0 0 535 223" preserveAspectRatio="none">
      <polyline points="0,2 267,120 535,2" fill="none" stroke="var(--paper-line)" stroke-width="1.2"/>
    </svg>
    <div class="brand">
      <span class="brand-dot" style="width:18px;height:18px"></span>
      <span class="brand-name" style="font-size:10px">VELANTRA</span>
    </div>
  </div>

  <div class="sheet env-front">
    <div class="band"></div>
    <div class="brand">
      <span class="brand-dot lifted" style="width:24px;height:24px"></span>
      <div class="brand-words"><span class="brand-name" style="font-size:15px">VELANTRA</span><span class="brand-tag" style="font-size:4.5px">MOBILE ULTRASOUND</span></div>
    </div>
    <div class="fine" style="left:20px;top:182px">
      <div><span class="icon"></span>P.O. Box 48617 Las Vegas, NV 89120-4861</div>
      <div><span class="icon"></span>702.555.0148 &nbsp;|&nbsp; info@velantramobilescan.example</div>
    </div>
    <div class="web" style="right:12px;top:192px">www.velantramobilescan.example</div>
  </div>

</div>
</body>
</html>
```